integrative health clinic-Medical massage, acupuncture, chiropractic

we like our logo, but are open to new ideas. We need a new card design. We have added chiropractic and acupuncture that we have put under the name of the business. We are an integrative medical clinic

Target Market(s)

General public, athletes

Contact Information for Business Card

Phone 5055583927
Fax 5055583926
Hours Monday-Friday 9-6
Saturday 10-6
The 20% can be smaller on the back

Colors
3176b5
0355a3

Requirements
Must have
• Logo but am open to ideas
Nice to have
• We are an integrated medical clinic but also want to be personable. We want the card fun and inviting

```html
<!DOCTYPE html>
<html lang="en">
<head>
<meta charset="utf-8">
<title>Clear Path Wellness – Business Card</title>
<link rel="stylesheet" href="https://fonts.googleapis.com/css2?family=Barlow:wght@400;500&family=Cinzel:wght@400&family=PT+Sans:wght@700&display=swap">
<style>
  :root {
    --brand-blue: #3176b5;
    --brand-navy: #0355a3;
    --silver-light: #ffffff;
    --silver-mid: #d6d6d6;
    --silver-dark: #9a9a9a;
    --ink: #2a2a2e;
    --white: #ffffff;
    --backdrop: #3a3a3a;
  }
  html, body {
    margin: 0;
    padding: 0;
    width: 1200px;
    height: 1200px;
    overflow: hidden;
    background: var(--backdrop);
  }
  .sheet { display: block; width: 1200px; height: 1200px; }
  .band-blue { fill: var(--brand-blue); }
  .band-navy { fill: var(--brand-navy); }
  .mark-circle { fill: url(#silver-soft); }
  .brand-title { font-family: "Barlow", sans-serif; font-weight: 500; fill: var(--white); }
  .tagline { font-family: "Barlow", sans-serif; font-weight: 400; fill: var(--ink); }
  .specializing { font-family: "Cinzel", serif; fill: var(--brand-navy); }
  .services { font-family: "PT Sans", sans-serif; font-weight: 700; fill: var(--brand-navy); }
  .hours { font-family: "PT Sans", sans-serif; font-weight: 700; fill: var(--brand-navy); }
  .contact { font-family: "Barlow", sans-serif; font-weight: 500; fill: var(--white); }
  .cross-blue { fill: var(--brand-blue); }
  .cross-silver { fill: url(#silver-linear); }
</style>
</head>
<body>
<svg class="sheet" viewBox="0 0 1200 1200" xmlns="http://www.w3.org/2000/svg">
  <defs>
    <radialGradient id="silver-band" cx="0.6" cy="0" r="0.75">
      <stop offset="0" stop-color="var(--silver-light)"/>
      <stop offset="0.55" stop-color="var(--silver-mid)"/>
      <stop offset="1" stop-color="var(--silver-dark)"/>
    </radialGradient>
    <linearGradient id="silver-linear" x1="0" y1="0" x2="1" y2="0">
      <stop offset="0" stop-color="#999"/>
      <stop offset="0.5" stop-color="#d8d8d8"/>
      <stop offset="1" stop-color="#a0a0a0"/>
    </linearGradient>
    <linearGradient id="silver-soft" x1="0" y1="1" x2="1" y2="0">
      <stop offset="0" stop-color="#a4a4a4"/>
      <stop offset="1" stop-color="#dcdcdc"/>
    </linearGradient>
    <clipPath id="back-clip"><rect width="843" height="475"/></clipPath>
  </defs>

  <!-- Front card -->
  <g class="card card-front" transform="translate(178 88)">
    <rect class="band-blue" width="843" height="218"/>
    <circle class="mark-circle" cx="160" cy="111" r="72"/>
    <text class="brand-title" x="279" y="103" font-size="50" textLength="500">CLEAR PATH WELLNESS</text>
    <text class="tagline" x="777" y="154" font-size="20" text-anchor="end" letter-spacing="0.5">The 20% can be smaller on the back</text>

    <rect y="218" width="843" height="196" fill="url(#silver-band)"/>
    <text class="specializing" x="37" y="290" font-size="36" textLength="584">SPECIALIZING IN</text>
    <text class="services" x="35" y="322" font-size="25" textLength="588">Medical Sports Massage And Manual Therapies</text>
    <text class="hours" x="35" y="361" font-size="14">HOURS</text>
    <text class="hours" x="35" y="385" font-size="14">MONDAY-FRIDAY 9-6 SATURDAY 10-6</text>
    <path class="cross-blue" d="M725 274h26v26h26v26h-26v26h-26v-26h-26v-26h26z"/>

    <rect class="band-blue" y="414" width="843" height="10"/>
    <rect class="band-navy" y="424" width="843" height="53"/>
    <text class="contact" x="35" y="454" font-size="21">Phone 5055583927 Fax 5055583926</text>
  </g>

  <!-- Back card -->
  <g class="card card-back" transform="translate(178 655)" clip-path="url(#back-clip)">
    <rect class="band-blue" width="843" height="408"/>
    <path class="cross-silver" d="M757 0h47v39h39v47h-39v41h-47v-41h-40v-47h40z"/>
    <circle class="mark-circle" cx="158" cy="202" r="72"/>
    <text class="brand-title" x="265" y="214" font-size="54" font-weight="400" textLength="484">Clear Path Wellness</text>
    <text class="tagline" x="271" y="255" font-size="30" font-weight="500" textLength="478">Medical &amp; Sports Massage</text>
    <rect y="408" width="843" height="30" fill="url(#silver-linear)"/>
    <rect class="band-navy" y="438" width="843" height="37"/>
  </g>
</svg>
</body>
</html>
```